Marnie Vale Photography needs a unique, creative business card/logo design

I need a design for business cards/logo that is unique and creative in the industry. Simplicity is nice, so not too crowded. Something that will catch my customer's eye and remain in their memory. I am primarily a landscape photographer but will be soon may be branching into boudoir photography as well. I have attached my current card.

Marnie Vale Photography
Phone: 0439 517 264
Email: MarnieValePhotography@quillmail.example
Website: www.snapnook.example/MarnieValePhotography.Aust

Marnie Vale Photography

• Contact Details on one side
• pixelation

```html
<!DOCTYPE html>
<html lang="en">
<head>
<meta charset="utf-8">
<title>Marnie Vale Photography – Business Card</title>
<link href="https://fonts.googleapis.com/css2?family=Jost:wght@300;400&display=swap" rel="stylesheet">
<style>
  :root {
    --page-bg: #d9d4ce;
    --card-dark: #161515;
    --card-dark-mid: #2b2827;
    --card-dark-edge: #45403d;
    --frost-light: #e6e1db;
    --frost-mid: #c9c1b8;
    --contact-text: #ebe6e0;
    --icon-fill: #d8d2cb;
    --brand-text: #2a2826;
  }
  * { margin: 0; padding: 0; box-sizing: border-box; }
  html, body {
    width: 1200px;
    height: 969px;
    overflow: hidden;
    background: var(--page-bg);
  }
  .canvas {
    position: relative;
    width: 1200px;
    height: 969px;
  }
  .business-card {
    position: absolute;
    left: 100px;
    top: 200px;
    width: 1000px;
    height: 570px;
    border-radius: 28px;
    overflow: hidden;
    box-shadow: 0 18px 40px rgba(0, 0, 0, 0.18);
  }
  .card-surface {
    position: absolute;
    inset: 0;
    width: 100%;
    height: 100%;
  }
  .contact-list {
    position: absolute;
    left: 46px;
    top: 208px;
    list-style: none;
    font-family: "Jost", sans-serif;
    font-weight: 300;
    font-size: 23px;
    color: var(--contact-text);
  }
  .contact-item {
    display: flex;
    align-items: center;
    height: 43px;
  }
  .contact-icon {
    width: 22px;
    height: 22px;
    margin-right: 16px;
    flex: none;
  }
  .brand-name {
    position: absolute;
    left: 574px;
    top: 226px;
    font-family: "Jost", sans-serif;
    font-weight: 300;
    font-size: 29px;
    letter-spacing: 0.55em;
    line-height: 52px;
    color: var(--brand-text);
    text-transform: uppercase;
    white-space: nowrap;
  }
  .brand-line { display: block; }
</style>
</head>
<body>
<main class="canvas">
  <article class="business-card">
    <svg class="card-surface" viewBox="0 0 1000 570" aria-hidden="true">
      <defs>
        <linearGradient id="darkFace" x1="0" y1="0" x2="1" y2="0.4">
          <stop offset="0" stop-color="var(--card-dark-edge)"/>
          <stop offset="0.25" stop-color="var(--card-dark)"/>
          <stop offset="0.7" stop-color="var(--card-dark-mid)"/>
          <stop offset="1" stop-color="var(--card-dark)"/>
        </linearGradient>
        <radialGradient id="frostArea" cx="0.6" cy="0.5" r="0.7">
          <stop offset="0" stop-color="var(--frost-light)"/>
          <stop offset="1" stop-color="var(--frost-mid)"/>
        </radialGradient>
      </defs>
      <rect width="1000" height="570" fill="url(#darkFace)"/>
    </svg>
    <svg class="card-surface" viewBox="0 0 1000 570" role="img" aria-label="Frosted translucent circle with a camera aperture illustration">
      <circle cx="950" cy="260" r="440" fill="url(#frostArea)"/>
    </svg>

    <ul class="contact-list">
      <li class="contact-item">
        <svg class="contact-icon" viewBox="0 0 24 24" aria-hidden="true">
          <path d="M6.6 2.5 9.5 6.2 7.8 8.6c1.3 2.9 3.5 5.2 6.4 6.6l2.4-1.7 3.8 2.9-1.6 3.7C11 19.8 4.2 13 3 4.1Z" fill="var(--icon-fill)"/>
        </svg>
        <span class="contact-text">0439 517 264</span>
      </li>
      <li class="contact-item">
        <svg class="contact-icon" viewBox="0 0 24 24" aria-hidden="true">
          <rect x="3" y="3" width="18" height="18" rx="2" fill="var(--icon-fill)"/>
        </svg>
        <span class="contact-text">MarnieValePhotography.Aust</span>
      </li>
      <li class="contact-item">
        <svg class="contact-icon" viewBox="0 0 24 24" aria-hidden="true">
          <circle cx="12" cy="12" r="9.5" fill="var(--icon-fill)"/>
        </svg>
        <span class="contact-text">MarnieValePhotography.Aust</span>
      </li>
      <li class="contact-item">
        <svg class="contact-icon" viewBox="0 0 24 24" aria-hidden="true">
          <rect x="2.5" y="5.5" width="19" height="13" fill="none" stroke="var(--icon-fill)" stroke-width="1.6"/>
          <path d="M2.5 5.5 12 13l9.5-7.5" fill="none" stroke="var(--icon-fill)" stroke-width="1.6"/>
        </svg>
        <span class="contact-text">MarnieValePhotography@quillmail.example</span>
      </li>
    </ul>

    <h1 class="brand-name">
      <span class="brand-line">Marnie Vale</span>
      <span class="brand-line">Photography</span>
    </h1>
  </article>
</main>
</body>
</html>
```